Website Design for NYC Female Attorney – Clean, Warm, Professional

Marian Thorpe, Esq.
www.MarianJThorpeLegal.example

I’m a New York City-based attorney and CPA with a reputation for providing thoughtful, high-integrity legal guidance in both estate planning and small business law. I’ve served over 500 clients, and maintain a perfect 5-star rating. Clients come to me for clarity, compassion, and results — and I want my new website to reflect that.

**🎯 WHAT I NEED:**
A clean, modern, and emotionally resonant website that highlights who I am, what I do, and why clients trust me. It must feel approachable and warm, but still professional and elegant — think Quillo meets boutique law firm. Feminine but not frilly.

**🧩 CORE WEBSITE SECTIONS (Top Navigation):**

1. **Home** – Strong first impression, tagline, CTA (book a call)
Homepage Copy (Sample Layout)
Headline:
Trusted Legal Guidance for Families and Founders.

Subheading:
Whether you’re protecting what you’ve built or building what’s next, I help you navigate estate planning and business law with confidence, compassion, and clarity.

Tagline (beneath logo or footer):
Legal Clarity for Life and Business.
2. **About Marian** – Bio, personal approach, credentials
3. **Services**

* *Estate Planning*
* *Business Law*
4. **Who I Work With** – Ideal clients (parents, entrepreneurs, etc.)
5. **Testimonials** – Client praise and social proof
6. **Success Stories** – Highlighting wins and case types
7. **FAQs** – Warm and clear answers to common questions
8. **Blog** – Thought leadership and helpful tips
8.5 Events
9. **Contact / Book a Call** – Scheduling or contact form

**🖼 STYLE DIRECTION:**

* Clean white backgrounds, soft jewel tones or neutrals
* Professional headshots and personal branding assets available
* Emphasis on readability, trust, and ease of navigation - THIS NEEDS TO BE BUILT OUT SO IT IS TRUSTED BY AI!
* No harsh colors, no corporate/legal clichés (e.g., gavels or scales) - I MEAN THIS. I DO NOT WANT A BORING LAW WEBSITE WITH SCALES AND GAVELS
* Feminine edge (not pink-heavy), with strong hierarchy and callouts

**💡 DESIGN NOTES:**

* Mobile-first design required
* Should include space for video or welcome message
* Easy to update blog or CMS area preferred
* Built in a user-friendly platform like WordPress, Webflow, or similar
* Needs to feel elevated enough to support high-end flat fee packages

**📣 TONE:**
Smart. Warm. Sophisticated. Human.

**⚖️ FINAL DELIVERABLES:**

* Homepage + 5+ interior pages
* Desktop + mobile views
* Style guide (fonts, colors, buttons)
* Bonus if you can help with copy layout/structure (not just visuals)

**📍TARGET AUDIENCE:**

* Busy professionals and families in NYC
* Women and couples who want peace of mind
* Entrepreneurs and creatives needing solid legal support

Here is my current site: www.MarianJThorpeLegal.example
And here is a second business I have: www.QuickCounselDaily.example

Families and business owners

Law

Serif
Sans Serif
Script

• This website must be built to be seen as trustworthy by AI.

```html
<!DOCTYPE html>
<html lang="en">
<head>
<meta charset="utf-8">
<title>Marian Thorpe – Law Office</title>
<link href="https://fonts.googleapis.com/css2?family=Playfair+Display:wght@500;600;700&family=Inter:wght@400;500;600&display=swap" rel="stylesheet">
<style>
:root{
  --navy:#3e4a7a;
  --pink:#ea8ba7;
  --pink-soft:#f6c9d6;
  --ink:#1f2233;
  --muted:#5d6070;
  --line:#e3e4ea;
  --wash:#f6f6f8;
  --backdrop:#c4c4c4;
  --white:#ffffff;
}
*{box-sizing:border-box;margin:0;padding:0}
html,body{width:1200px;height:4107px;overflow:hidden;background:var(--backdrop)}
body{font-family:"Inter",Arial,sans-serif;color:var(--ink);position:relative}
.serif{font-family:"Playfair Display",Georgia,serif}
.page{position:absolute;left:255px;top:92px;width:741px;height:3920px;background:var(--white);overflow:hidden}
section,header{position:relative;width:741px}
.abs{position:absolute}
.photo{position:absolute}
.eyebrow{position:absolute;font-size:7px;font-weight:600;color:var(--pink)}
.btn-pink{position:absolute;background:var(--pink);color:#fff;font-size:7.5px;border-radius:2px;display:flex;align-items:center;justify-content:center;gap:4px;white-space:nowrap}
.btn-navy{position:absolute;background:var(--navy);color:#fff;font-size:7.5px;border-radius:2px;display:flex;align-items:center;justify-content:center;gap:4px;white-space:nowrap}
.small{font-size:7.5px;line-height:1.55;color:var(--muted)}

/* top bar */
.topbar{height:23px;background:var(--navy)}
.topbar .accent{position:absolute;left:622px;top:0;width:119px;height:23px;background:var(--pink)}
.topbar .info{position:absolute;right:132px;top:0;height:23px;display:flex;align-items:center;gap:12px;color:#fff;font-size:6.5px;white-space:nowrap}
.topbar .info span{display:flex;align-items:center;gap:4px}
.topbar .social{position:absolute;right:28px;top:7px;display:flex;gap:3px}
.topbar .social i{width:9px;height:9px;border-radius:50%;background:#fff;display:block}

/* brand name */
.brand{position:absolute;display:flex;align-items:center;gap:6px;white-space:nowrap;font-family:"Playfair Display",Georgia,serif;font-weight:500;letter-spacing:1px}
.brand i{display:block;border-radius:50%;background:var(--pink)}

/* nav */
.nav{height:51px;border-bottom:1px solid var(--line)}
.nav .brand{left:75px;top:17px;font-size:12px;color:var(--navy)}
.nav .brand i{width:9px;height:9px}
.nav ul{position:absolute;left:268px;top:21px;display:flex;gap:14px;list-style:none;font-size:8px;white-space:nowrap}
.nav .btn-navy{left:606px;top:17px;width:60px;height:18px}

/* hero */
.hero{height:291px;background:linear-gradient(90deg,#f1f1ef 0%,#ececea 45%,#dcd9d6 100%)}
.hero h1{position:absolute;left:75px;top:52px;font-size:22px;line-height:32px;font-weight:600;color:var(--ink);white-space:nowrap}
.hero p{position:absolute;left:75px;top:124px;width:290px;font-size:8px;line-height:14px;color:var(--muted)}
.hero .btn-pink{left:75px;top:181px;width:72px;height:18px}

/* about */
.about{height:488px}
.about h2{position:absolute;left:386px;top:100px;font-size:30px;font-weight:700;white-space:nowrap}
.years{position:absolute;left:230px;top:86px;width:126px;height:89px;background:var(--pink);border-radius:8px;box-shadow:-7px 7px 0 var(--navy);color:#fff;text-align:center;font-family:"Playfair Display",serif;font-size:27px;line-height:30px;padding-top:13px}
.about .para{position:absolute;left:386px;width:285px;font-size:8px;line-height:12.5px;color:var(--muted)}
.about h4{position:absolute;left:386px;top:262px;font-size:8px;font-weight:600}
.approach{position:absolute;display:flex;align-items:center;gap:8px;font-size:7.5px;font-weight:600;line-height:11px;color:var(--navy);white-space:nowrap}
.approach i{width:28px;height:28px;border-radius:50%;background:var(--navy);display:block}
.about .btn-pink{left:386px;top:386px;width:108px;height:18px}

/* services */
.services{height:188px;background:var(--navy);color:#fff}
.services h3{position:absolute;left:75px;top:32px;font-size:18px;font-weight:500}
.services .li{position:absolute;font-size:7.5px;color:#fff;white-space:nowrap}
.services .li::before{content:"•";color:var(--pink);margin-right:6px}
.circ{position:absolute;width:18px;height:18px;border-radius:50%;background:rgba(255,255,255,.25);display:flex;align-items:center;justify-content:center}

/* who */
.who{height:377px;background:var(--wash)}
.center-h{position:absolute;left:0;width:741px;text-align:center;font-weight:600;color:var(--ink)}
.card{position:absolute;top:159px;width:140px;height:134px;background:#fff;border:1px solid var(--line);border-radius:8px;padding:14px 11px}
.card.dark{background:var(--navy);border-color:var(--navy);color:#fff}
.card .ic{width:26px;height:26px;border:1.5px solid var(--navy);border-radius:6px}
.card.dark .ic{border-color:#fff}
.card h5{font-family:"Playfair Display",serif;font-size:8.5px;line-height:11px;margin-top:12px;font-weight:600}
.card.dark h5{color:var(--pink-soft)}
.card p{font-size:6.3px;line-height:9px;color:var(--muted);margin-top:4px;padding-right:14px}
.card.dark p{color:#dfe2ee}
.card .go{position:absolute;right:6px;bottom:6px;width:20px;height:20px;border-radius:50%;background:var(--pink)}

/* testimonials */
.testi{height:307px}
.tcard{position:absolute;top:152px;width:192px;height:109px;border:1px solid var(--line);border-radius:6px;background:#fff;text-align:center;padding:36px 14px 0;border-bottom:3px solid var(--line)}
.tcard.dark{background:var(--navy);color:#fff;border-color:var(--navy)}
.tcard .av{position:absolute;left:77px;top:-21px;width:38px;height:38px;border-radius:50%;background:#d5d7dd;border:2px solid var(--pink)}
.tcard .nm{font-family:"Playfair Display",serif;font-size:7px;color:var(--pink)}
.tcard .st{font-size:7px;color:#f0b33c;letter-spacing:1px}
.tcard p{font-size:6px;line-height:9px;color:var(--muted);margin-top:3px}
.tcard.dark p{color:#e2e5f0}
.tcard .tail{position:absolute;right:14px;bottom:-9px;width:0;height:0;border-left:8px solid transparent;border-top:8px solid var(--pink)}

/* results */
.results{height:281px}

/* faq */
.faq{height:306px;background:var(--navy)}
.faq h3{position:absolute;left:75px;top:60px;font-size:15px;color:#fff;font-weight:500;white-space:nowrap}
.q{position:absolute;height:22px;background:#fff;border-radius:2px;display:flex;align-items:center;justify-content:space-between;padding:0 9px;font-family:"Playfair Display",serif;font-size:7px;font-weight:600;white-space:nowrap}
.q b{font-family:"Inter",sans-serif;font-size:11px;font-weight:500}
.q.open{height:68px;align-items:flex-start;flex-direction:column;justify-content:flex-start;padding-top:6px;white-space:normal}
.q.open .row{display:flex;justify-content:space-between;width:100%;white-space:nowrap}
.q.open p{font-family:"Inter",sans-serif;font-weight:400;font-size:5.8px;line-height:8.5px;color:var(--muted);margin-top:6px;border-top:1px solid var(--line);padding-top:5px}

/* blogs */
.blogs{height:558px}
.blogs h3{position:absolute;left:75px;top:90px;font-size:17px;font-weight:600}
.viewall{position:absolute;font-size:8px;text-decoration:underline;color:var(--ink);white-space:nowrap}
.bcard{position:absolute;border:1px solid var(--line);border-radius:6px;background:#fff;overflow:hidden}
.bcard .date{font-size:6.5px;color:var(--pink)}
.bcard h4{font-family:"Playfair Display",serif;font-weight:600}
.dot{position:absolute;width:18px;height:18px;border-radius:50%;background:#c9ccd6}

/* events */
.events{height:346px;background:var(--wash)}
.events h3{position:absolute;left:75px;top:44px;font-size:18px;line-height:25px;font-weight:600}
.ecard{position:absolute;left:75px;width:278px;background:#fff;border:1px solid #c7cad5;border-radius:5px;font-size:12px;font-weight:600;color:var(--navy);line-height:15px}
.ecard .tri{position:absolute;right:9px;top:7px;width:0;height:0;border-left:4px solid transparent;border-right:4px solid transparent}

/* contact */
.contact{height:470px}
.form{position:absolute;left:389px;top:89px;width:277px;height:293px;background:#f7f7f9;border-radius:0 6px 6px 0;padding:20px 17px}
.form h4{font-family:"Playfair Display",serif;font-size:12px;font-weight:600}
.form .lbl{font-size:6.5px;margin-top:12px}
.form .fld{height:15px;background:#fff;border:1px solid var(--line);border-radius:2px;margin-top:4px;font-size:5.5px;color:#b8bac4;padding:4px 6px}

/* footer */
.footer{height:234px;background:var(--navy);color:#fff}
.footer .brand{left:75px;top:38px;font-size:16px;color:#fff}
.footer .brand i{width:11px;height:11px}
.footer .col{position:absolute;top:117px;font-size:6.8px;line-height:18px;white-space:nowrap}
.footer .col h6{font-family:"Playfair Display",serif;color:var(--pink);font-size:9px;font-weight:500;line-height:14px;margin-bottom:2px}
.footer .col .ar::before{content:"↗";margin-right:6px;font-size:7px}
.fsoc{position:absolute;top:41px;width:20px;height:20px;border-radius:50%;background:#fff}
</style>
</head>
<body>
<main class="page">

  <!-- top bar -->
  <div class="topbar" style="position:relative">
    <div class="accent"></div>
    <div class="info">
      <span><svg width="7" height="8" viewBox="0 0 7 8"><path d="M3.5 0a3 3 0 0 0-3 3c0 2.2 3 5 3 5s3-2.8 3-5a3 3 0 0 0-3-3z" fill="#ea8ba7"/></svg>48 Linden Row, Fl 9 New York, NY 10099</span>
      <span><svg width="8" height="6" viewBox="0 0 8 6"><rect x=".5" y=".5" width="7" height="5" fill="none" stroke="#fff"/><path d="M.5.5l3.5 3 3.5-3" fill="none" stroke="#fff"/></svg>marian@marianthorpelegal.example</span>
      <span><svg width="7" height="7" viewBox="0 0 7 7"><path d="M1 0l1.5 1.8-.8 1a4 4 0 0 0 2.3 2.3l1-.8L7 6 6 7C3 7 0 4 0 1z" fill="#ea8ba7"/></svg>(212) 555-0147</span>
    </div>
    <div class="social"><i></i><i></i><i></i></div>
  </div>

  <!-- nav -->
  <header class="nav">
    <div class="brand"><i></i>MARIAN THORPE</div>
    <ul><li>Home</li><li>About Marian</li><li>Services</li><li>Who I Work</li><li>Testimonials</li><li>FAQs</li><li>Blog</li></ul>
    <div class="btn-navy">Contact <span>⟶</span></div>
  </header>

  <!-- hero -->
  <section class="hero">
    <div class="photo" role="img" aria-label="Portrait of the attorney seated in a bright office" style="left:446px;top:0;width:295px;height:291px;background:linear-gradient(160deg,#e4dfdb 0%,#cdbfb4 45%,#5b4a43 80%,#d8d2cc 100%)"></div>
    <h1 class="serif">Trusted Legal Guidance<br>for Families and Founders.</h1>
    <p>Whether you’re protecting what you’ve built or building what’s next, I help you navigate estate planning and business law with confidence, compassion, and clarity.</p>
    <div class="btn-pink">Schedule a Call</div>
  </section>

  <!-- about -->
  <section class="about">
    <div class="photo" role="img" aria-label="Hand holding a magnifying glass over a glowing growth chart" style="left:75px;top:108px;width:130px;height:292px;border-radius:8px;background:linear-gradient(160deg,#2a3a6e,#4c6aa8 45%,#1c2650)"></div>
    <div class="years">9+<br>Years</div>
    <div class="photo" role="img" aria-label="Portrait of the attorney in a denim jacket" style="left:225px;top:196px;width:131px;height:184px;border-radius:8px;background:linear-gradient(170deg,#c9c6c2,#8d7e74 55%,#4f6180)"></div>
    <div class="eyebrow" style="left:386px;top:86px;color:var(--navy)">About Marian</div>
    <h2 class="serif">Meet Marian</h2>
    <p class="para" style="top:144px">Hi, <b style="color:var(--ink)">I’m Marian—a lawyer</b>, parent, and advocate for clarity in the legal process. I started this practice to make estate planning and business law feel less intimidating and more empowering.</p>
    <p class="para" style="top:196px">With [X] years of experience, a JD from [Law School], and deep roots in this community, I take pride in providing thoughtful, responsive, and plain-English legal advice. My mission is to help you make confident decisions that protect your family, your future, and your legacy.</p>
    <h4>My Approach</h4>
    <div class="approach" style="left:386px;top:297px"><i></i>Thoughtful, not<br>transactional.</div>
    <div class="approach" style="left:571px;top:297px"><i></i>Strategic, not<br>stuffy.</div>
    <div class="approach" style="left:386px;top:345px"><i></i>Compassionate,<br>not cold.</div>
    <div class="approach" style="left:571px;top:345px"><i></i>Grounded, not<br>rigid.</div>
    <div class="btn-pink">Read More About Me <span>⟶</span></div>
  </section>

  <!-- services -->
  <section class="services">
    <div class="eyebrow" style="left:75px;top:18px">Services</div>
    <h3 class="serif">Estate Planning</h3>
    <div class="abs" style="left:75px;top:70px;font-size:7.5px;white-space:nowrap">Create peace of mind with a plan built for your family and your future.</div>
    <div class="abs" style="left:75px;top:96px;font-size:7.5px;color:var(--pink);font-weight:600">Services include:</div>
    <div class="li" style="left:75px;top:121px">Wills and Trusts</div>
    <div class="li" style="left:255px;top:121px">Health Care Directives</div>
    <div class="li" style="left:75px;top:140px">Powers of Attorney</div>
    <div class="li" style="left:255px;top:140px">Guardianship Planning</div>
    <div class="li" style="left:75px;top:159px">Estate Administration Support</div>
    <div class="circ" style="left:37px;top:87px"><svg width="6" height="8"><path d="M5 1L1 4l4 3" fill="none" stroke="#fff"/></svg></div>
    <div class="photo" role="img" aria-label="Modern apartment building against a blue sky" style="left:386px;top:0;width:355px;height:188px;background:linear-gradient(180deg,#6fa6dc 0%,#a9cbe9 40%,#d8d3cb 60%,#5a6c62 100%)"></div>
  </section>

  <!-- who -->
  <section class="who">
    <div class="center-h" style="top:51px;font-size:7px;color:var(--pink);font-family:Inter,sans-serif">Who I Work With</div>
    <div class="center-h serif" style="top:68px;font-size:18px;line-height:25px">Legal Solutions for Visionaries, Caregivers,<br>and Legacy-Builders</div>
    <div class="abs" style="left:75px;top:134px;font-size:7.5px">I work best with:</div>
    <div class="card dark" style="left:75px"><div class="ic"></div><h5>Parents and<br>Families</h5><p>Plans that protect your children, your home and the people who count on you most, written in clear words.</p><div class="go"></div></div>
    <div class="card" style="left:226px"><div class="ic"></div><h5>Entrepreneurs<br>and Founders</h5><p>Sound structure, contracts and advice so your new venture can grow on steady ground from day one.</p><div class="go"></div></div>
    <div class="card" style="left:377px"><div class="ic"></div><h5>Blended<br>Families</h5><p>Careful planning that honours every relationship and keeps each member of the family looked after.</p><div class="go"></div></div>
    <div class="card" style="left:526px"><div class="ic"></div><h5>Established Business<br>Owners</h5><p>Succession, protection and growth plans for companies that have already earned their place.</p><div class="go"></div></div>
    <div class="abs" style="left:75px;top:316px;font-size:7.5px;white-space:nowrap">If you value clarity, integrity, and a personal relationship with your attorney, you’re in the right place.</div>
  </section>

  <!-- testimonials -->
  <section class="testi">
    <div class="center-h serif" style="top:86px;font-size:18px">Testimonials</div>
    <div class="tcard dark" style="left:75px"><div class="av"></div><div class="nm">Dana Wexley</div><div class="st">★★★★★</div><p>“It was such a pleasure working with Marian. My financial planner suggested I get an estate plan and I am so glad I did. She answered all questions.”</p><div class="tail"></div></div>
    <div class="tcard" style="left:274px"><div class="av"></div><div class="nm">Priya Halden</div><div class="st">★★★★★</div><p>“Marian is the expert in this practice. She is kind, patient, knowledgeable and professional. I trust her guidance and recommend her to anyone.”</p><div class="tail"></div></div>
    <div class="tcard" style="left:474px"><div class="av"></div><div class="nm">Owen Castell</div><div class="st">★★★★★</div><p>“Marian helped me get my will and power of attorney drawn up and I couldn’t be happier. She explained everything and answered every question.”</p><div class="tail"></div></div>
  </section>

  <!-- results -->
  <section class="results">
    <div class="center-h" style="top:54px;font-size:7px;color:var(--pink);font-family:Inter,sans-serif">Who I Work With</div>
    <div class="center-h serif" style="top:72px;font-size:18px">Real Results, Real Peace of Mind</div>
    <div class="photo" role="img" aria-label="Smiling business owner working at a laptop" style="left:0;top:103px;width:383px;height:178px;background:linear-gradient(90deg,#ffffff 0%,#e7ecf3 35%,#7f9bc6 55%,#e9edf3 80%,#ffffff 100%)"></div>
    <p class="abs" style="left:386px;top:151px;width:280px;font-size:7.5px;line-height:12px;color:var(--muted)">Working with Marian gave our family a real plan and real calm. Every step was explained, every question answered, and we left knowing exactly what would happen next.</p>
    <div class="abs" style="left:495px;top:203px;font-size:7px;color:var(--pink);font-weight:600">Client Name</div>
    <div class="abs" style="left:497px;top:212px;font-size:5px;color:var(--muted)">Small Business</div>
    <div class="circ" style="left:37px;top:160px;background:#cfd2da"><svg width="6" height="8"><path d="M5 1L1 4l4 3" fill="none" stroke="#fff"/></svg></div>
    <div class="circ" style="left:686px;top:160px;background:#cfd2da"><svg width="6" height="8"><path d="M1 1l4 3-4 3" fill="none" stroke="#fff"/></svg></div>
  </section>

  <!-- faq -->
  <section class="faq">
    <div class="eyebrow" style="left:75px;top:43px">FAQs</div>
    <h3 class="serif">You Have Questions. I Have Answers.</h3>
    <div class="q open" style="left:75px;top:98px;width:280px"><div class="row"><span>01.&nbsp;&nbsp;&nbsp;What are the initial steps to get started?</span><b>−</b></div><p>When you are ready to move forward, we will first agree on an engagement letter and fee by secure online payment. Once the housekeeping items are taken care of, you will schedule your first design meeting.</p></div>
    <div class="q" style="left:75px;top:174px;width:280px"><span>02.&nbsp;&nbsp;&nbsp;What is estate planning?</span><b>+</b></div>
    <div class="q" style="left:75px;top:204px;width:280px"><span>03.&nbsp;&nbsp;&nbsp;How much does estate planning cost?</span><b>+</b></div>
    <div class="q" style="left:75px;top:235px;width:280px"><span>04.&nbsp;&nbsp;&nbsp;How long does the process take?</span><b>+</b></div>
    <div class="q" style="left:386px;top:46px;width:280px"><span>05.&nbsp;&nbsp;&nbsp;Can I sign my documents with e-signature?</span><b>+</b></div>
    <div class="q" style="left:386px;top:76px;width:280px"><span>06.&nbsp;&nbsp;&nbsp;What kind of clients do you accept?</span><b>+</b></div>
    <div class="q" style="left:386px;top:107px;width:280px"><span>07.&nbsp;&nbsp;&nbsp;Why do I need a living trust?</span><b>+</b></div>
    <div class="q" style="left:386px;top:137px;width:280px"><span>08.&nbsp;&nbsp;&nbsp;Isn’t estate planning just for the wealthy?</span><b>+</b></div>
    <div class="q" style="left:386px;top:168px;width:280px"><span>09.&nbsp;&nbsp;&nbsp;I’m not married – do I need an estate plan?</span><b>+</b></div>
    <div class="q" style="left:386px;top:198px;width:280px"><span>10.&nbsp;&nbsp;&nbsp;Do you work with families in all 50 states?</span><b>+</b></div>
    <div class="q" style="left:386px;top:229px;width:280px"><span>11.&nbsp;&nbsp;&nbsp;Can’t I just do my will on a video call?</span><b>+</b></div>
  </section>

  <!-- blogs -->
  <section class="blogs">
    <h3 class="serif">Blogs</h3>
    <div class="viewall" style="left:630px;top:97px">view All</div>
    <div class="bcard" style="left:75px;top:128px;width:278px;height:303px">
      <div role="img" aria-label="Team meeting in a bright modern office" style="height:134px;background:linear-gradient(180deg,#d9d4cd,#a9917e 60%,#6e7d94)"></div>
      <div style="padding:12px 16px">
        <div class="date">October 23, 2024</div>
        <h4 style="font-size:13px;line-height:18px;margin-top:4px">What Every Business Owner<br>Should Know About Contracts</h4>
        <p class="small" style="font-size:6.5px;line-height:10px;margin-top:8px">A clear contract protects your time, your money and your relationships. Here are the clauses every owner should read twice, and the questions worth asking before anyone signs on the line.</p>
        <p class="small" style="font-size:6.5px;line-height:10px;margin-top:5px">Small details now can prevent large disputes later, so start with the basics.</p>
      </div>
    </div>
    <div class="bcard" role="img" aria-label="Two colleagues reviewing documents together" style="left:391px;top:128px;width:275px;height:134px;background:linear-gradient(120deg,#2e3546,#6a7282 50%,#b9a89a)">
      <div style="position:absolute;left:13px;top:10px;color:#fff">
        <div style="font-size:6.5px">October 23, 2024</div>
        <div class="serif" style="font-size:12px;line-height:16px;font-weight:600;margin-top:3px">LLC vs. S-Corp: What’s<br>Right for You?</div>
      </div>
    </div>
    <div class="bcard" style="left:391px;top:282px;width:126px;height:149px">
      <div role="img" aria-label="Apartment building facade" style="height:68px;background:linear-gradient(180deg,#6fa6dc,#c9c4bb 70%,#6a7a6e)"></div>
      <div style="padding:8px 8px"><div class="date" style="font-size:5px">October 23, 2024</div><h4 style="font-size:8.5px;line-height:11px;margin-top:4px">5 Myths About<br>Estate Planning</h4></div>
    </div>
    <div class="bcard" style="left:541px;top:282px;width:125px;height:149px">
      <div role="img" aria-label="Hands signing a document" style="height:68px;background:linear-gradient(135deg,#eef1f6,#9fb0cc 60%,#dfe3ea)"></div>
      <div style="padding:8px 8px"><div class="date" style="font-size:5px">October 23, 2024</div><h4 style="font-size:8.5px;line-height:11px;margin-top:4px">Why Legal Planning<br>Is an Act of Love</h4></div>
    </div>
    <div class="dot" style="left:349px;top:450px"></div>
    <div class="dot" style="left:373px;top:450px"></div>
  </section>

  <!-- events -->
  <section class="events">
    <div class="eyebrow" style="left:75px;top:28px">Events</div>
    <h3 class="serif">Upcoming Events &amp;<br>Workshops</h3>
    <div class="ecard" style="top:100px;height:87px">
      <div role="img" aria-label="Presenter speaking with attendees" style="position:absolute;left:0;top:0;width:81px;height:85px;border-radius:4px 0 0 4px;background:linear-gradient(160deg,#d6d2cc,#8b8177 60%,#4d5466)"></div>
      <div style="position:absolute;left:96px;top:26px;width:170px">“Business Law Basics for New Entr epreneurs”</div>
      <div class="tri" style="border-top:6px solid var(--pink)"></div>
    </div>
    <div class="ecard" style="top:199px;height:38px;padding:5px 10px">“Business Law Basics for New Entrepreneurs”<div class="tri" style="border-bottom:6px solid var(--pink)"></div></div>
    <div class="ecard" style="top:249px;height:38px;padding:5px 10px">“Business Law Basics for New Entrepreneurs”<div class="tri" style="border-bottom:6px solid var(--pink)"></div></div>
    <div class="viewall" style="left:317px;top:312px">view All</div>
    <div class="abs" style="left:459px;top:27px;width:207px;height:273px;background:var(--pink);border-radius:8px"></div>
    <div class="photo" role="img" aria-label="Audience attending a workshop seminar" style="left:386px;top:43px;width:266px;height:262px;border-radius:6px;background:linear-gradient(180deg,#eef0f2 0%,#cfd3d8 35%,#555b66 70%,#2d3240 100%)"></div>
  </section>

  <!-- contact -->
  <section class="contact">
    <div class="photo" role="img" aria-label="Smiling assistant wearing a headset at a desk" style="left:75px;top:89px;width:314px;height:293px;border-radius:6px 0 0 6px;background:linear-gradient(120deg,#3c4150,#8d8a86 45%,#e2dcd3 80%)"></div>
    <div class="form">
      <h4>Let’s Get Started</h4>
      <p class="small" style="font-size:7px;line-height:11px;margin-top:8px;color:var(--ink)">Whether you’re ready to move forward or just have questions,<br>I’d love to connect.</p>
      <div class="lbl">Name</div><div class="fld">Your name</div>
      <div style="display:flex;gap:34px">
        <div style="flex:1"><div class="lbl">Email</div><div class="fld">Your email</div></div>
        <div style="flex:1"><div class="lbl">Phone No</div><div class="fld">Your phone</div></div>
      </div>
      <div class="lbl">Message</div><div class="fld" style="height:56px">Message</div>
      <div style="margin-top:16px;width:50px;height:17px;background:var(--navy);color:#fff;font-size:7px;display:flex;align-items:center;justify-content:center;border-radius:2px">Submit ⟶</div>
    </div>
  </section>

  <!-- footer -->
  <footer class="footer" style="position:relative;width:741px">
    <div class="brand"><i></i>MARIAN THORPE</div>
    <div class="abs serif" style="left:75px;top:70px;font-size:7.5px;font-weight:600;white-space:nowrap">Legal Clarity for Life and Business.</div>
    <div class="fsoc" style="left:559px"></div><div class="fsoc" style="left:584px"></div><div class="fsoc" style="left:609px"></div><div class="fsoc" style="left:634px"></div>
    <div class="abs" style="left:75px;top:99px;width:591px;height:1px;background:rgba(255,255,255,.35)"></div>
    <div class="col" style="left:75px"><h6>Quick Links</h6><div class="ar">Home</div><div class="ar">About Marian</div><div class="ar">Services</div></div>
    <div class="col" style="left:199px"><h6>Quick Links</h6><div class="ar">Who I Work</div><div class="ar">Testimonials</div><div class="ar">Contact</div></div>
    <div class="col" style="left:338px"><h6>Contact Us</h6><div>☏&nbsp; (212) 555-0147</div><div>✉&nbsp; marian@marianthorpelegal.example</div><div style="line-height:9px;margin-top:4px">⌖&nbsp; 48 Linden Row, Fl 9<br>&nbsp;&nbsp;&nbsp;&nbsp;New York, NY 10099</div></div>
    <div class="col" style="left:510px;top:117px"><div class="serif" style="font-size:14px;line-height:18px">Subscribe for Marian<br>J. Thorpe</div>
      <div style="position:relative;margin-top:12px;width:156px;height:18px;background:#fff;border-radius:9px;color:#999;font-size:5.5px;line-height:18px;padding-left:9px">Enter Your Email<span style="position:absolute;right:0;top:0;width:46px;height:18px;border-radius:9px;background:var(--pink);color:#fff;text-align:center">Submit</span></div></div>
    <div class="abs" style="left:0;top:216px;width:741px;text-align:center;font-size:6.5px">Copyright © 2025 On Marian J. Thorpe All Rights Reserved.</div>
  </footer>

</main>
</body>
</html>
```